Website for The Tavery Parlour

I require a website for "The Tavery Parlour" which is a blog type business for 40+ year old women covering books, true crime, history, travel and food. It needs to support blog posts, links to social media including YouTube videos, Instagram, TikTok and Facebook. The background theme needs to be like that of a newspaper. Easy to navigate and to allow me to post blogs/videos.

```html
<!DOCTYPE html>
<html lang="en">
<head>
<meta charset="utf-8">
<title>The Tavery Parlour</title>
<link href="https://fonts.googleapis.com/css2?family=Source+Serif+4:opsz,wght@8..60,400;8..60,600;8..60,700&family=Inter:wght@400&display=swap" rel="stylesheet">
<style>
  :root {
    --ink: #0b0b0b;
    --paper: #ffffff;
    --rule-soft: #b9b9b9;
    --rule: #1a1a1a;
    --muted: #555555;
    --studio-a: #c9a27a;
    --studio-b: #6f7fa8;
    --studio-c: #a9b3bf;
    --room-a: #8d8f93;
    --room-b: #c8c2b0;
    --room-c: #e3e6ea;
  }
  * { box-sizing: border-box; margin: 0; padding: 0; }
  html, body {
    width: 1200px; height: 1032px; overflow: hidden;
    background: var(--paper); color: var(--ink);
    font-family: "Source Serif 4", Georgia, serif;
  }
  .site { position: relative; width: 1200px; height: 1032px; }

  .topbar {
    position: absolute; left: 0; top: 0; width: 1200px; height: 113px;
    border-bottom: 2px solid var(--rule-soft);
  }
  .menu-button {
    position: absolute; left: 557px; top: 42px; width: 97px; height: 45px;
    border: 1.5px solid var(--ink); background: var(--paper);
    display: flex; align-items: center; justify-content: center; gap: 8px;
    font-family: "Inter", Arial, sans-serif; font-size: 15px; color: var(--ink);
  }
  .account-links { position: absolute; top: 52px; left: 0; width: 100%; }
  .account-links a {
    position: absolute; color: var(--ink); text-decoration: none;
    font-size: 16px; font-weight: 600; letter-spacing: 0.02em; text-transform: uppercase;
  }

  .masthead {
    position: absolute; left: 0; top: 115px; width: 1200px; height: 248px;
    display: flex; align-items: center; justify-content: center;
  }
  .masthead-title {
    font-size: 104px; font-weight: 400; letter-spacing: -0.035em; line-height: 1;
    color: var(--ink);
  }

  .section-nav {
    position: absolute; left: 0; top: 363px; width: 1200px; height: 67px;
    border-top: 1.5px solid var(--rule); border-bottom: 1.5px solid var(--rule);
  }
  .section-nav a {
    position: absolute; top: 0; height: 100%;
    display: flex; align-items: center; justify-content: center;
    color: var(--ink); text-decoration: none; font-size: 26px; font-weight: 700;
  }
  .section-nav a + a { border-left: 1.5px solid var(--rule); }

  .featured-divider {
    position: absolute; left: 781px; top: 430px; width: 2px; height: 602px;
    background: var(--rule-soft);
  }
  .featured-heading {
    position: absolute; left: 68px; top: 446px;
    font-size: 39px; font-weight: 700; line-height: 1;
  }
  .post-meta {
    position: absolute; font-size: 11px; color: var(--muted);
    letter-spacing: 0.02em; text-transform: uppercase;
  }
  .lead-image {
    position: absolute; left: 68px; top: 504px; width: 702px; height: 528px;
    background: linear-gradient(100deg, var(--studio-a) 0%, var(--studio-b) 35%, var(--studio-c) 60%, var(--studio-c) 100%);
  }
  .side-image {
    position: absolute; left: 793px; top: 497px; width: 341px; height: 535px;
    background: linear-gradient(90deg, var(--room-a) 0%, var(--room-b) 45%, var(--room-c) 100%);
  }
</style>
</head>
<body>
<div class="site">
  <header class="topbar">
    <button class="menu-button" type="button">Menu
      <svg width="14" height="13" viewBox="0 0 14 13" aria-hidden="true">
        <rect x="1" y="1" width="12" height="4.5" rx="1" fill="none" stroke="#0b0b0b" stroke-width="1.2"/>
        <rect x="1" y="7.5" width="12" height="4.5" rx="1" fill="none" stroke="#0b0b0b" stroke-width="1.2"/>
      </svg>
    </button>
    <nav class="account-links">
      <a href="#" style="left:817px">Search</a>
      <a href="#" style="left:937px">Sign in</a>
      <a href="#" style="left:1052px">Sign up</a>
    </nav>
  </header>

  <div class="masthead">
    <h1 class="masthead-title">The Tavery Parlour</h1>
  </div>

  <nav class="section-nav">
    <a href="#" style="left:0;width:241px;padding-left:60px">Books</a>
    <a href="#" style="left:241px;width:284px">True Crime</a>
    <a href="#" style="left:525px;width:228px">History</a>
    <a href="#" style="left:753px;width:228px">Travel</a>
    <a href="#" style="left:981px;width:219px">Food</a>
  </nav>

  <main>
    <h2 class="featured-heading">Featured</h2>
    <span class="post-meta" style="left:700px;top:466px">22 Jun 2024</span>
    <div class="lead-image" role="img" aria-label="Painting studio with abstract canvases leaning against a grey wall"></div>

    <div class="featured-divider"></div>

    <span class="post-meta" style="left:793px;top:466px">Art Market</span>
    <span class="post-meta" style="left:1064px;top:466px">22 Jun 2024</span>
    <div class="side-image" role="img" aria-label="Bright room with a framed botanical painting and flowers beside tall windows"></div>
  </main>
</div>
</body>
</html>
```